Retractable Banner Stands

Hello we need a deisgn for a banner.
Sizes: 36"x80", 12"x17"(this one to have less on it, most the logo, license numvber, and address), and a 24"x40" banner
Roofing Services
HOA & Commercial Roofing
• Emergency roof tarping & repairs — Starting at $550
• Small & large roof repairs
• Preventative roof maintenance
• Full roof replacement
Deck & Balcony Services
• Balcony & deck maintenance
SB-326 Repairs
• Deck resurfacing
• Small & large deck repairs
• Full deck reconstruction
Gutter Services
• Small & large gutter repairs
• Gutter cleaning & maintenance
• New gutter installation & replacement
License Information:
C-39 Roofing Contractor
General B Contractor
License #4729351
📍 Serving Orange County & Surrounding Areas
📍 Office Location:
5 Brantwick Road, Suite K
HOA & Commerical roofs
Roofing
- Gotham

```html
<!DOCTYPE html>
<html lang="en">
<head>
<meta charset="utf-8">
<title>Corvane Roofing & Waterproofing – Banner Stands</title>
<link href="https://fonts.googleapis.com/css2?family=Montserrat:wght@500;600;700;800&display=swap" rel="stylesheet">
<style>
  :root{
    --brand-blue:#04a7e8;
    --ink:#231f20;
    --ink-soft:#2b2b2b;
    --paper:#ffffff;
    --stage-top:#ffffff;
    --stage-bottom:#9ec8f1;
    --font:'Montserrat', Arial, sans-serif;
  }
  *{box-sizing:border-box;margin:0;padding:0}
  html,body{width:1200px;height:675px;overflow:hidden}
  body{
    position:relative;
    font-family:var(--font);
    background:linear-gradient(180deg,var(--stage-top) 0%,var(--stage-bottom) 100%);
    color:var(--ink);
  }
  .banner{position:absolute;top:69px;height:536px;overflow:hidden;box-shadow:0 6px 18px rgba(0,40,90,.18)}
  .abs{position:absolute}
  .brand{color:var(--paper);display:flex;flex-direction:column;align-items:center}
  .brand-name{font-weight:800;letter-spacing:.02em;line-height:1;display:flex;align-items:center;gap:.18em}
  .brand-dot{display:inline-block;width:.28em;height:.28em;background:var(--brand-blue)}
  .brand-tag{font-weight:600;letter-spacing:.01em;white-space:nowrap}

  /* ---------- Tall banner ---------- */
  .banner--tall{left:96px;width:241px;background:var(--paper)}
  .tall-photo{left:0;top:110px;width:100%;height:360px;
    background:linear-gradient(160deg,#eef2f4 0%,#dfe7e2 35%,#e6e2dc 70%,#efe9e4 100%)}
  .tall-header{left:0;top:0;width:100%;height:130px}
  .tall-header .brand{position:absolute;left:0;right:0;top:20px}
  .tall-header .brand-name{font-size:36px}
  .tall-header .brand-tag{font-size:10.5px;margin-top:8px}
  .tall-titles{left:0;right:0;top:128px;text-align:center;font-weight:600;font-size:16.5px;line-height:20px}
  .tall-license{left:49px;top:186px;width:144px;height:34px;border-radius:17px;background:var(--brand-blue);
    color:var(--paper);font-weight:700;font-size:27px;line-height:34px;text-align:center}
  .tall-number{left:0;right:0;text-align:center;color:var(--brand-blue);font-weight:800;font-size:90px;line-height:84px;letter-spacing:-.03em}
  .tall-number--a{top:230px}
  .tall-number--b{top:316px}
  .tall-serving{left:0;right:0;top:413px;text-align:center;font-weight:600;font-size:13.5px;line-height:17px}
  .tall-footer{left:0;top:450px;width:100%;height:86px}
  .tall-footer-text{left:0;right:0;top:470px;text-align:center;color:var(--paper);font-weight:600}
  .tall-footer-text .label{font-size:16px;line-height:20px}
  .tall-footer-text .addr{font-size:14px;line-height:20px;margin-top:7px}

  /* ---------- Poster ---------- */
  .banner--poster{left:371px;width:378px;background:var(--paper)}
  .poster-photo{left:0;top:0;width:100%;height:181px;
    background:linear-gradient(135deg,#2c3533 0%,#454c4f 40%,#5b6166 65%,#3a4340 100%)}
  .poster-photo::after{content:"";position:absolute;inset:0;background:rgba(20,20,20,.35)}
  .poster-head{left:28px;top:30px;z-index:1}
  .poster-head .brand{align-items:flex-start}
  .poster-head .brand-name{font-size:38px;padding-left:20px}
  .poster-head .brand-tag{font-size:11.5px;margin-top:10px}
  .poster-titles{left:28px;top:104px;color:var(--paper);font-weight:700;font-size:24.5px;line-height:30px;z-index:1}
  .poster-license{left:0;top:201px;width:206px;height:53px;border-radius:0 27px 27px 0;background:var(--brand-blue);
    color:var(--paper);font-weight:700;font-size:37px;line-height:53px;padding-left:26px}
  .poster-number{left:26px;top:268px;color:var(--brand-blue);font-weight:800;font-size:74px;line-height:86px;letter-spacing:-.02em}
  .poster-footer{left:0;top:352px;width:100%;height:184px;background:var(--brand-blue);color:var(--ink);padding:16px 28px 0}
  .poster-footer .serving{font-weight:600;font-size:23px;line-height:29px}
  .poster-footer .label{font-weight:600;font-size:21px;line-height:25px;color:var(--paper);margin-top:20px}
  .poster-footer .addr{font-weight:600;font-size:21px;line-height:27px;color:var(--paper);white-space:nowrap}

  /* ---------- Services banner ---------- */
  .banner--services{left:782px;width:322px;background:var(--paper)}
  .svc-header{left:0;top:0;width:322px;height:194px}
  .svc-head-brand{left:22px;top:18px}
  .svc-head-brand .brand-name{font-size:28px;padding-left:14px}
  .svc-head-brand .brand-tag{font-size:8.5px;margin-top:6px}
  .svc-titles{left:24px;top:80px;color:var(--paper);font-weight:700;font-size:18.5px;line-height:18.5px}
  .svc-license{left:24px;top:122px;color:var(--brand-blue);font-weight:700;font-size:12.5px}
  .svc-serving{left:24px;top:141px;color:var(--paper);font-weight:500;font-size:10px}
  .svc-location{left:166px;top:158px;color:var(--brand-blue);font-weight:600;font-size:9.5px;line-height:12.5px}
  .svc-location .addr{font-size:10.5px}
  .svc-heading{left:19px;top:192px;font-weight:800;font-size:21px;line-height:21px}
  .svc-heading span{color:var(--brand-blue)}
  .svc-col-head{color:var(--brand-blue);font-weight:700;font-size:8.8px;line-height:11.5px;bottom:auto}
  .svc-rule{left:16px;top:280px;width:289px;height:1.5px;background:var(--brand-blue)}
  .svc-list{list-style:none;font-weight:600;font-size:7.3px;line-height:11px}
  .svc-list li{padding-left:6px;position:relative}
  .svc-list li::before{content:"•";position:absolute;left:0}
  .svc-photo{top:370px;height:166px;
    background:linear-gradient(160deg,#c9d2da 0%,#8e9aa6 50%,#5e6a6b 100%)}
  .svc-photo--a{left:0;width:118px;clip-path:polygon(0 36px,118px 24px,118px 166px,0 166px)}
  .svc-photo--b{left:116px;width:100px;clip-path:polygon(0 24px,100px 14px,100px 166px,0 166px);
    background:linear-gradient(160deg,#9ab6c8 0%,#6f7a5d 45%,#6a4d3c 100%)}
  .svc-photo--c{left:214px;width:108px;clip-path:polygon(0 14px,108px 0,108px 166px,0 166px);
    background:linear-gradient(160deg,#b9c5d1 0%,#7c8894 55%,#4d5558 100%)}
</style>
</head>
<body>

<!-- Tall retractable banner -->
<section class="banner banner--tall">
  <div class="abs tall-photo" role="img" aria-label="Faded photo of a roofer working on a tiled residential roof"></div>
  <svg class="abs tall-header" viewBox="0 0 241 130" preserveAspectRatio="none" aria-hidden="true">
    <path d="M0 0H241V118Q120 100 0 120Z" fill="var(--ink)"/>
  </svg>
  <div class="tall-header abs">
    <div class="brand">
      <div class="brand-name">CORVANE<span class="brand-dot"></span></div>
      <div class="brand-tag">ROOFING &amp; WATERPROOFING</div>
    </div>
  </div>
  <div class="abs tall-titles">C-39 Roofing Contractor<br>General B Contractor</div>
  <div class="abs tall-license">License</div>
  <div class="abs tall-number tall-number--a">4729</div>
  <div class="abs tall-number tall-number--b">351</div>
  <div class="abs tall-serving">Serving Orange County &amp;<br>Surrounding Areas</div>
  <svg class="abs tall-footer" viewBox="0 0 241 86" preserveAspectRatio="none" aria-hidden="true">
    <path d="M0 10Q120 -4 241 10V86H0Z" fill="var(--brand-blue)"/>
  </svg>
  <div class="abs tall-footer-text">
    <div class="label">Location</div>
    <div class="addr">5 Brantwick Road, Suite K</div>
  </div>
</section>

<!-- Small poster -->
<section class="banner banner--poster">
  <div class="abs poster-photo" role="img" aria-label="Aerial photo of a commercial building roof under repair"></div>
  <div class="abs poster-head">
    <div class="brand">
      <div class="brand-name">CORVANE<span class="brand-dot"></span></div>
      <div class="brand-tag">ROOFING &amp; WATERPROOFING</div>
    </div>
  </div>
  <div class="abs poster-titles">C-39 Roofing Contractor<br>General B Contractor</div>
  <div class="abs poster-license">License</div>
  <div class="abs poster-number">4729351</div>
  <div class="abs poster-footer">
    <div class="serving">Serving Orange County &amp;<br>Surrounding Areas</div>
    <div class="label">Location</div>
    <div class="addr">5 Brantwick Road, Suite K</div>
  </div>
</section>

<!-- Services banner -->
<section class="banner banner--services">
  <svg class="abs svc-header" viewBox="0 0 322 194" aria-hidden="true">
    <path d="M0 0H322V194H152L134 178H0Z" fill="var(--ink)"/>
  </svg>
  <div class="abs svc-head-brand">
    <div class="brand">
      <div class="brand-name">CORVANE<span class="brand-dot"></span></div>
      <div class="brand-tag">ROOFING &amp; WATERPROOFING</div>
    </div>
  </div>
  <div class="abs svc-titles">C-39 Roofing Contractor<br>General B Contractor</div>
  <div class="abs svc-license">License : 4729351</div>
  <div class="abs svc-serving">Serving Orange County &amp; Surrounding Areas</div>
  <div class="abs svc-location">Location<br><span class="addr">5 Brantwick Road, Suite K</span></div>

  <h2 class="abs svc-heading">ROOFING<br><span>SERVICES</span></h2>

  <div class="abs svc-col-head" style="left:22px;top:242px">HOA &amp;<br>COMMERCIAL<br>ROOFING</div>
  <div class="abs svc-col-head" style="left:119px;top:242px">DECK &amp;<br>BALCONY<br>SERVICES</div>
  <div class="abs svc-col-head" style="left:212px;top:265px">GUTTER SERVICES</div>
  <div class="abs svc-rule"></div>

  <ul class="abs svc-list" style="left:22px;top:286px;width:92px">
    <li>Emergency roof tarping &amp; repairs — Starting at $550</li>
    <li>Small &amp; large roof repairs</li>
    <li>Preventative roof maintenance</li>
    <li>Full roof replacement</li>
  </ul>
  <ul class="abs svc-list" style="left:119px;top:286px;width:90px">
    <li>Balcony &amp; deck maintenance SB-326 Repairs</li>
    <li>Deck resurfacing</li>
    <li>Small &amp; large deck repairs</li>
    <li>Full deck reconstruction</li>
  </ul>
  <ul class="abs svc-list" style="left:212px;top:289px;width:80px">
    <li>Small &amp; large gutter repairs</li>
    <li>Gutter cleaning &amp; maintenance</li>
    <li>New gutter installation &amp; replacement</li>
  </ul>

  <div class="abs svc-photo svc-photo--a" role="img" aria-label="Aerial photo of an apartment complex roof"></div>
  <div class="abs svc-photo svc-photo--b" role="img" aria-label="Photo of a roofer in safety harness repairing tiles"></div>
  <div class="abs svc-photo svc-photo--c" role="img" aria-label="Aerial photo of a flat commercial roof"></div>
</section>

</body>
</html>
```